Website for Apartment Rental in Prague

I would like to create designs of my website focused on luxury apartment rentals in Prague, Czech Republic. I created initial mock-ups, They are all attached. I need to design homepage and subpage. The mock-ups were created by combining elements from different websites that I liked but I need you to create a design that is unique and original. The attached files a only a guidance for the structure of the website but not for the design. Try to be creative.

Industry/Entity Type

Apartment

```html
<!DOCTYPE html>
<html lang="en">
<head>
<meta charset="utf-8">
<title>Velour Apartments Prague</title>
<link href="https://fonts.googleapis.com/css2?family=Hind:wght@300;400;500;600&family=Noto+Serif:ital,wght@0,400;1,400;1,700&display=swap" rel="stylesheet">
<style>
:root{
  --gold:#bfae7b;
  --gold-dark:#a8965f;
  --ink:#222222;
  --text:#5a5a5a;
  --muted:#8a8a8a;
  --line:#e2e2e2;
  --strip:#ededed;
  --footer:#262626;
  --white:#ffffff;
}
*{box-sizing:border-box;margin:0;padding:0}
html,body{width:1200px;height:2799px;overflow:hidden}
body{position:relative;background:var(--white);font-family:'Hind',sans-serif;color:var(--text)}
.abs{position:absolute}

/* top bar */
.topbar{left:0;top:0;width:1200px;height:37px;background:var(--ink);display:flex;justify-content:center;align-items:center;gap:30px;color:#e6e6e6;font-size:13px}
.topbar span{display:flex;align-items:center;gap:6px}
.topbar svg{width:13px;height:13px;fill:none;stroke:#e6e6e6;stroke-width:1.6}

/* header */
.brand{left:0;top:37px;width:1200px;height:97px;display:flex;justify-content:center;align-items:center;gap:10px}
.brand-mark{width:14px;height:14px;border-radius:50%;background:var(--gold)}
.brand-name{font-family:'Hind',sans-serif;font-weight:500;font-size:19px;letter-spacing:4px;color:var(--ink);text-transform:uppercase}
.nav{left:0;top:134px;width:1200px;height:41px;border-top:1px solid var(--line);display:flex;justify-content:center;gap:38px;font-size:13.5px;letter-spacing:.6px;color:#555;text-transform:uppercase}
.nav a{position:relative;display:flex;align-items:center;height:41px;color:inherit;text-decoration:none}
.nav a.active{color:var(--gold)}
.nav a.active::before{content:"";position:absolute;left:-6px;right:-6px;top:-1px;height:3px;background:var(--gold)}

/* hero */
.hero{left:0;top:175px;width:1200px;height:514px;background:linear-gradient(100deg,#1d1d1f 0%,#3a3633 30%,#55504a 48%,#8e8c88 62%,#4a4745 78%,#2a2a2b 100%)}
.hero-title{left:0;top:322px;width:1200px;text-align:center;font-weight:600;font-size:40px;letter-spacing:.5px;color:var(--white);text-transform:uppercase}
.offer-tab{left:112px;top:528px;width:354px;height:43px;background:var(--gold);color:var(--white);font-size:16px;display:flex;align-items:center;padding-left:16px;border-top-right-radius:40px}
.booking{left:112px;top:571px;width:976px;height:90px;background:var(--white);padding:16px 16px 0 16px}
.field{position:absolute;top:16px}
.field label{display:block;font-size:11px;color:var(--muted);margin-bottom:5px}
.box{height:36px;border:1px solid #d8d8d8;display:flex;align-items:center;padding:0 8px;font-size:13px;color:#444;justify-content:space-between}
.box svg{width:18px;height:18px;fill:none;stroke:#aaa;stroke-width:1.4}
.caret{width:0;height:0;border-left:4px solid transparent;border-right:4px solid transparent;border-top:5px solid #888}
.check-btn{position:absolute;left:627px;top:37px;width:150px;height:36px;background:var(--gold);color:var(--white);font-size:13px;display:flex;align-items:center;justify-content:center;text-transform:uppercase}
.or{position:absolute;left:787px;top:47px;font-size:13px;color:#666}

/* intro */
.kicker{left:0;top:734px;width:1200px;text-align:center;font-weight:300;font-size:24px;letter-spacing:5px;color:#333;text-transform:uppercase}
.script-title{left:0;top:758px;width:1200px;text-align:center;font-family:'Noto Serif',serif;font-style:italic;font-weight:700;font-size:46px;color:var(--ink)}
.rule{left:564px;top:826px;width:72px;height:2px;background:var(--gold)}
.lede{left:100px;width:1000px;text-align:center;font-family:'Noto Serif',serif;font-style:italic;font-size:15.5px;color:#666;line-height:24px}
.emblem{left:577px;top:985px;width:46px;height:46px;border:1.5px solid var(--gold);border-radius:50%;display:flex;align-items:center;justify-content:center}
.emblem svg{width:22px;height:22px;fill:none;stroke:var(--gold);stroke-width:1.5}
.emblem-title{left:0;top:1046px;width:1200px;text-align:center;font-size:16px;font-weight:500;color:var(--ink);line-height:24px}
.emblem-title em{font-style:normal;color:var(--gold)}
.about{left:128px;top:1116px;width:944px;text-align:center;font-size:14.5px;line-height:23px;color:#666}

/* cards */
.card{width:308px}
.card-photo{position:relative;width:308px;height:220px}
.price{position:absolute;right:8px;top:8px;background:var(--white);padding:5px 10px 3px;font-size:13px;color:#333}
.price i{font-family:'Noto Serif',serif;font-size:12px}
.price b{font-weight:600}
.spec{display:flex;height:38px;background:var(--strip);font-size:13px;color:#444}
.spec div{flex:1;display:flex;align-items:center;justify-content:center}
.spec div+div{border-left:1px solid #d6d6d6}
.card-title{margin-top:21px;text-align:center;font-size:16.5px;font-weight:500;color:var(--ink);line-height:23px}
.card-desc{margin-top:12px;text-align:center;font-size:14px;color:#777}
.btn{display:flex;align-items:center;justify-content:center;height:34px;font-size:13px;color:var(--white);text-transform:uppercase;letter-spacing:.4px}
.btn-dark{margin-top:16px;background:var(--ink)}
.btn-gold{margin-top:10px;background:var(--gold)}

/* need to know */
.section-head{left:0;top:2266px;width:1200px;text-align:center;font-size:23px;letter-spacing:4px;color:#333;text-transform:uppercase;font-weight:400}
.fact{width:300px;text-align:center}
.fact svg{width:56px;height:60px;fill:none;stroke:var(--gold);stroke-width:2}
.fact h3{margin-top:6px;font-size:16px;font-weight:500;color:var(--ink)}
.fact p{margin-top:8px;font-size:14px;line-height:24px;color:#666}
.fact p b{font-weight:600;color:#444}

/* footer */
.footer{left:0;top:2545px;width:1200px;height:254px;background:var(--footer);color:#dcdcdc}
.footer h4{position:absolute;font-size:18px;font-weight:400;color:var(--white)}
.footer .small{position:absolute;font-size:12.5px;line-height:21px;color:#cfcfcf}
.footer .phone{position:absolute;left:112px;top:155px;font-size:26px;font-weight:300;color:var(--white)}
.social{position:absolute;left:862px;top:82px;display:flex;gap:6px}
.social span{width:32px;height:32px;border:1.5px solid #cfcfcf;border-radius:50%}
.message{position:absolute;left:864px;top:213px;width:224px;height:41px;background:var(--gold);border-top-left-radius:8px;border-top-right-radius:8px;display:flex;align-items:center;justify-content:center;gap:8px;font-size:14px;font-weight:500;color:var(--white)}
.message svg{width:16px;height:16px;fill:none;stroke:var(--white);stroke-width:1.6}
</style>
</head>
<body>

<div class="abs topbar">
  <span><svg viewBox="0 0 14 14"><path d="M2 10h10M3 10a4 4 0 0 1 8 0M7 4v2"/></svg>Our Hospitality</span>
  <span><svg viewBox="0 0 14 14"><path d="M1 3l4-1.5 4 1.5 4-1.5v9.5l-4 1.5-4-1.5-4 1.5z"/></svg>Discover Prague</span>
  <span><svg viewBox="0 0 14 14"><rect x="1" y="3" width="12" height="8"/><path d="M1 3l6 5 6-5"/></svg>reservation@velourstays.com</span>
  <span><svg viewBox="0 0 14 14"><path d="M3 1.5l2.5 2.5-1.5 1.5a7 7 0 0 0 4.5 4.5L10 8.5l2.5 2.5-1.5 1.5C6 12 2 8 1.5 3z"/></svg>420 600 555 218</span>
  <span>En ▾</span>
</div>

<header class="abs brand">
  <span class="brand-mark"></span>
  <span class="brand-name">Velour Apartments Prague</span>
</header>

<nav class="abs nav">
  <a class="active">Apartments</a><a>Location</a><a>Services</a><a>Gallery</a><a>News</a><a>Exclusive Offers &amp; Tours</a><a>For Families</a><a>Contact Us</a>
</nav>

<div class="abs hero" role="img" aria-label="Photograph of a modern apartment living room with a dark leather sofa, dining table and large windows"></div>
<h1 class="abs hero-title">Being Home in Prague</h1>
<div class="abs offer-tab">Official Site - Best Price Guaranteed</div>
<form class="abs booking">
  <div class="field" style="left:16px;width:116px"><label>Check in date</label><div class="box">11/17/2017<svg viewBox="0 0 18 18"><rect x="2" y="3" width="14" height="13"/><path d="M2 7h14M6 1v4M12 1v4"/></svg></div></div>
  <div class="field" style="left:144px;width:116px"><label>Check out date</label><div class="box">11/18/2017<svg viewBox="0 0 18 18"><rect x="2" y="3" width="14" height="13"/><path d="M2 7h14M6 1v4M12 1v4"/></svg></div></div>
  <div class="field" style="left:272px;width:52px"><label>Adults</label><div class="box">2<span class="caret"></span></div></div>
  <div class="field" style="left:336px;width:52px"><label>Children</label><div class="box">0<span class="caret"></span></div></div>
  <div class="field" style="left:400px;width:52px"><label>Infants</label><div class="box">0<span class="caret"></span></div></div>
  <div class="field" style="left:464px;width:152px"><label>Promotional code</label><div class="box"></div></div>
  <div class="check-btn">Check Availability</div>
  <div class="or">OR</div>
  <div class="field" style="left:812px;width:150px;top:37px"><div class="box" style="font-size:12px">Select Rental Unit<span class="caret"></span></div></div>
</form>

<h2 class="abs kicker">A Different Vision of</h2>
<div class="abs script-title">Travelling</div>
<div class="abs rule"></div>
<p class="abs lede" style="top:857px">Something spectacular has arrived in the heart of europe.</p>
<p class="abs lede" style="top:904px">Steps from old town, this rental experience is curated with world-class amenities, exemplary style and a level of convenience you have to experience to believe. Experience the different vision of luxury in center of prague.</p>

<div class="abs emblem"><svg viewBox="0 0 22 22"><path d="M7 3h8l2 8H5z M11 11v6M7 19h8"/></svg></div>
<div class="abs emblem-title">Interiors Designed<br>by <em>Velour</em></div>
<p class="abs about">Velour apartments offers short term and as well as long term options in our studio apartments and our one bedroom apartment homes. Our luxurious apartments and high quality customer service have allowed us to dominate the Prague apartment market with a proven track record. Our years of experience and knowledge have made us a premier apartment rental company as we continue to stress the importance of servicing individuals and corporations who are seeking the finest accommodations.</p>

<!-- apartments row 1 -->
<article class="abs card" style="left:112px;top:1269px">
  <div class="card-photo" role="img" aria-label="Photograph of a bright open-plan living room with white sofas and wooden floor" style="background:linear-gradient(160deg,#e8e4de,#b9a58c 60%,#8a6a4c)"><div class="price"><i>From</i> <b>150 USD</b></div></div>
  <div class="spec"><div>1 Bedroom</div><div>Max 4 People</div></div>
  <h3 class="card-title">Brand New Luxury Living<br>Stunning Contemporary Design</h3>
  <p class="card-desc">The 22nd issue is dedicated to colors...</p>
  <div class="btn btn-dark">Details</div><div class="btn btn-gold">Book Now</div>
</article>
<article class="abs card" style="left:446px;top:1269px">
  <div class="card-photo" role="img" aria-label="Photograph of a living room with grey walls, tall windows and a beige sofa" style="background:linear-gradient(160deg,#6d6468,#c9c2bb 50%,#8a7665)"><div class="price"><i>From</i> <b>150 USD</b></div></div>
  <div class="spec"><div>1 Bedroom</div><div>Max 4 People</div></div>
  <h3 class="card-title">Brand New Luxury Living<br>Stunning Contemporary Design</h3>
  <p class="card-desc">The 22nd issue is dedicated to colors...</p>
  <div class="btn btn-dark">Details</div><div class="btn btn-gold">Book Now</div>
</article>
<article class="abs card" style="left:780px;top:1269px">
  <div class="card-photo" role="img" aria-label="Photograph of a warmly lit bedroom with a large bed and wood panelling" style="background:linear-gradient(160deg,#3b2a1e,#8c6a46 50%,#d8c6a8)"><div class="price"><i>From</i> <b>150 USD</b></div></div>
  <div class="spec"><div>1 Bedroom</div><div>Max 4 People</div></div>
  <h3 class="card-title">Brand New Luxury Living<br>Stunning Contemporary Design</h3>
  <p class="card-desc">The 22nd issue is dedicated to colors...</p>
  <div class="btn btn-dark">Details</div><div class="btn btn-gold">Book Now</div>
</article>

<!-- apartments row 2 -->
<article class="abs card" style="left:112px;top:1750px">
  <div class="card-photo" role="img" aria-label="Photograph of a white loft living room with wooden floor and a wall decoration" style="background:linear-gradient(160deg,#eeeae4,#c9b89c 55%,#7c8a5a)"><div class="price"><i>From</i> <b>150 USD</b></div></div>
  <div class="spec"><div>1 Bedroom</div><div>Max 4 People</div></div>
  <h3 class="card-title">Brand New Luxury Living<br>Stunning Contemporary Design</h3>
  <p class="card-desc">The 22nd issue is dedicated to colors...</p>
  <div class="btn btn-dark">Details</div><div class="btn btn-gold">Book Now</div>
</article>
<article class="abs card" style="left:446px;top:1750px">
  <div class="card-photo" role="img" aria-label="Photograph of a white interior with a fireplace, plants and a floating staircase" style="background:linear-gradient(160deg,#f2efea,#d9cbb3 55%,#9b7b55)"><div class="price"><i>From</i> <b>150 USD</b></div></div>
  <div class="spec"><div>1 Bedroom</div><div>Max 4 People</div></div>
  <h3 class="card-title">Brand New Luxury Living<br>Stunning Contemporary Design</h3>
  <p class="card-desc">The 22nd issue is dedicated to colors...</p>
  <div class="btn btn-dark">Details</div><div class="btn btn-gold">Book Now</div>
</article>
<article class="abs card" style="left:780px;top:1750px">
  <div class="card-photo" role="img" aria-label="Photograph of a living room with a grey sofa, large windows and wooden floor" style="background:linear-gradient(160deg,#8c9aa3,#b8b2a6 50%,#a4784a)"><div class="price"><i>From</i> <b>150 USD</b></div></div>
  <div class="spec"><div>1 Bedroom</div><div>Max 4 People</div></div>
  <h3 class="card-title">Brand New Luxury Living<br>Stunning Contemporary Design</h3>
  <p class="card-desc">The 22nd issue is dedicated to colors...</p>
  <div class="btn btn-dark">Details</div><div class="btn btn-gold">Book Now</div>
</article>

<h2 class="abs section-head">Need to Know</h2>
<div class="abs fact" style="left:117px;top:2338px">
  <svg viewBox="0 0 56 60"><rect x="8" y="12" width="20" height="44"/><rect x="28" y="24" width="20" height="32"/><path d="M13 20h4M19 20h4M13 28h4M19 28h4M13 36h4M19 36h4M33 32h4M39 32h4M33 40h4M39 40h4M4 56h48"/></svg>
  <h3>Apartments</h3>
  <p>Also avaliable to rent all the apartmets<br>together for companies or larger groups.</p>
</div>
<div class="abs fact" style="left:450px;top:2338px">
  <svg viewBox="0 0 56 60"><rect x="12" y="16" width="32" height="36" rx="2"/><path d="M22 16V8h12v8M20 24v20M28 24v20M36 24v20M18 52v4M38 52v4"/></svg>
  <h3>Check-Out</h3>
  <p>12 noon; earliest check-in, 3pm- both are<br>flexible, by arrangement.</p>
</div>
<div class="abs fact" style="left:783px;top:2338px">
  <svg viewBox="0 0 56 60"><circle cx="28" cy="30" r="24"/><path d="M34 21c-2-3-12-3-12 3s12 3 12 9-10 6-12 2M28 15v30"/></svg>
  <h3>Rates</h3>
  <p>Prices from <b>150 USD</b> per night.<br>Including tax.</p>
</div>

<footer class="abs footer">
  <h4 style="left:112px;top:40px">Contact Us</h4>
  <p class="small" style="left:112px;top:74px">Velour Apartments Prague<br>228, lorem ipsum dolor sit,<br>osis amet it 85965</p>
  <div class="phone">420 600 555 218</div>
  <p class="small" style="left:112px;top:189px">reservation@velourstays.com</p>

  <h4 style="left:444px;top:40px">Quick Links</h4>
  <p class="small" style="left:444px;top:74px">Apartments<br>Location<br>Services<br>Gallery<br>News</p>
  <p class="small" style="left:562px;top:74px">Exclusive Offers &amp; Tours<br>For Families<br>Contact Us</p>

  <h4 style="left:862px;top:40px">Stay Connected</h4>
  <div class="social"><span></span><span></span><span></span><span></span><span></span></div>
  <p class="small" style="left:862px;top:149px">© 2017 Velour Apartments Prague.</p>
  <div class="message"><svg viewBox="0 0 16 16"><path d="M2 3h12v8H6l-4 3z"/></svg>Please Leave A Message</div>
</footer>

</body>
</html>
```